Modern Quillby Tree Care Website

I need a website for a full service Tree Care company. The company provides tree pruning, tree removal, tree preservation, emergency services, stump grinding, and emergency tree services.

Target Market(s)

Customers that need tree services

Industry/Entity Type

Landscaping, Tree Services

Coding

Coded - Design and coding required

Number of Pages Required

5+ page

Font styles to use
Sans Serif

Requirements
Must have
• Good clean design that showcases the services the company provides.
Nice to have
• Services page; contact form, blog, home page, about page

```html
<!DOCTYPE html>
<html lang="en">
<head>
<meta charset="utf-8">
<title>Quillby Tree Care</title>
<link href="https://fonts.googleapis.com/css2?family=Poppins:wght@400;500;600;700&display=swap" rel="stylesheet">
<style>
:root{
  --green:#7cc242;
  --lime:#dcf7c4;
  --orange:#f7a531;
  --brown:#c49a6c;
  --slate:#5f6b70;
  --forest:#1e4a14;
  --forest-deep:#163a0e;
  --ink:#222;
  --muted:#555;
  --white:#fff;
}
*{margin:0;padding:0;box-sizing:border-box}
html,body{width:1200px;height:5367px;overflow:hidden}
body{font-family:"Poppins",sans-serif;color:var(--ink);background:#fff;position:relative}
.abs{position:absolute}
/* hero */
.hero{left:0;top:0;width:1200px;height:760px;background:linear-gradient(180deg,#203d12 0%,#2f5a1b 40%,#3d6a22 75%,#4a7a2a 100%)}
.hero-circle{left:228px;top:110px;width:744px;height:744px;border-radius:50%;background:rgba(124,194,66,.55)}
.nav{left:0;top:0;width:1200px;height:110px}
.logo{left:72px;top:30px;display:flex;align-items:center;gap:12px;color:var(--white);font-weight:700;font-size:22px;letter-spacing:1px;line-height:1.1}
.logo-mark{width:46px;height:46px;background:var(--white)}
.menu{right:72px;top:46px;display:flex;gap:34px;font-size:13px;color:var(--white);font-weight:500}
.menu .active{color:var(--green);border-bottom:2px solid var(--green);padding-bottom:10px}
.hero-title{left:0;width:1200px;top:300px;text-align:center;color:var(--white);font-weight:600;font-size:58px;line-height:70px}
.hero-sub{left:0;width:1200px;top:458px;text-align:center;color:var(--white);font-weight:500;font-size:31px}
.btn{display:inline-flex;align-items:center;justify-content:center;border-radius:40px;color:var(--white);font-weight:600;text-transform:uppercase}
.hero-btn{left:502px;top:543px;width:196px;height:58px;background:var(--green);border:3px solid var(--white);font-size:14px}
/* features */
.features{left:104px;top:698px;width:996px;height:225px;background:var(--white);padding:10px;display:flex}
.feature{flex:1;color:var(--white);text-align:center;padding:28px 16px 0}
.feature h3{font-size:12.5px;font-weight:600;margin:16px 0 8px;line-height:1.25}
.feature p{font-size:12px;line-height:1.4}
.ficon{width:58px;height:58px;border-radius:50%;border:3px solid var(--white);margin:0 auto}
.f1{background:var(--brown)}.f2{background:var(--green)}.f3{background:var(--orange)}.f4{background:var(--slate)}.f5{background:var(--green)}
/* headings */
.sec-title{font-weight:600;font-size:48px;color:var(--green);text-transform:uppercase}
.sec-title::after{content:"";display:block;width:70px;height:3px;background:var(--orange);margin-top:10px}
.center{text-align:center;left:0;width:1200px}
.center.sec-title::after{margin:10px auto 0;width:124px}
/* about */
.about-title{left:100px;top:1068px}
.about-text{left:100px;top:1183px;width:445px;font-size:13px;line-height:27px;color:var(--muted);text-align:justify}
.about-text p+p{margin-top:27px}
.about-btn{left:100px;top:1448px;width:156px;height:48px;background:var(--green);font-size:12px}
.about-img{left:586px;top:1025px;width:516px;height:516px;border-radius:50%;background:radial-gradient(circle,#6fb23a,#5a9a2c)}
/* services */
.services-title{top:1670px}
.service{width:340px;text-align:center}
.service .pic{position:relative;height:300px}
.service .bg{position:absolute;left:95px;top:0;width:314px;height:300px;border-radius:50%;background:var(--lime)}
.service .photo{position:absolute;left:48px;top:40px;width:272px;height:272px;border-radius:50%}
.service h4{font-weight:500;font-size:24px;margin-top:20px}
.p1{background:linear-gradient(135deg,#b9cce0,#4d6a3a)}
.p2{background:linear-gradient(135deg,#5d4a30,#2f4a1e)}
.p3{background:linear-gradient(135deg,#6b5540,#3c5a2a)}
.p4{background:linear-gradient(135deg,#5c7a3a,#7a6540)}
.p5{background:linear-gradient(135deg,#5a4630,#c9622a)}
.p6{background:linear-gradient(135deg,#4a6a3a,#8a9a80)}
/* cta */
.cta-band{left:0;top:2760px;width:1200px;height:615px}
.cta-text{top:2910px;color:var(--white);font-weight:600;font-size:52px;line-height:65px;text-shadow:0 3px 6px rgba(0,0,0,.45)}
.cta-btn{left:477px;top:3150px;width:246px;height:72px;background:var(--orange);font-size:22px;font-weight:500}
/* blog */
.blog-title{top:3530px}
.card{top:3670px;width:277px;height:413px;background:var(--white);border-radius:10px;box-shadow:0 4px 14px rgba(0,0,0,.15);padding:7px;text-align:center}
.card .thumb{height:206px;border-radius:8px}
.card h5{font-weight:500;font-size:16px;line-height:22px;margin:28px 8px 14px}
.card p{font-size:12px;line-height:22px;color:var(--muted);margin:0 12px}
.card .btn{margin-top:24px;width:110px;height:28px;background:var(--green);font-size:10px;font-weight:500}
.t1{background:linear-gradient(135deg,#6b5a44,#3e5a2c)}
.t2{background:linear-gradient(135deg,#4d5a3a,#8a6a4a)}
.t3{background:linear-gradient(135deg,#c89a60,#7a5a3c)}
.dots{left:548px;top:4154px;display:flex;gap:12px;align-items:center}
.dots span{width:11px;height:11px;border-radius:50%;background:#cfcfcf}
.dots .on{width:28px;height:6px;border-radius:3px;background:var(--orange)}
/* contact */
.contact-bg{left:0;top:4256px;width:1200px;height:720px}
.contact-title{top:4365px;color:var(--white);font-weight:600;font-size:52px;text-transform:uppercase}
.contact-title::after{content:"";display:block;width:124px;height:3px;background:var(--white);margin:10px auto 0}
.field{background:var(--white);font-size:12px;color:#999;padding:12px 20px;border-radius:2px}
.submit{left:516px;top:4702px;width:167px;height:48px;background:var(--orange);font-size:16px;font-weight:500}
/* footer */
.footer{left:0;top:4916px;width:1200px;height:417px;background:var(--forest)}
.newsletter{left:206px;top:4939px;width:790px;height:111px;background:var(--orange);border-radius:60px;display:flex;align-items:center;padding:0 30px 0 34px;gap:14px}
.newsletter h3{color:var(--white);font-weight:600;font-size:32px;white-space:nowrap}
.nl-input{flex:1;height:42px;background:var(--white);border-radius:24px;display:flex;align-items:center;justify-content:space-between;padding:0 6px 0 22px;font-size:10px;color:#666}
.nl-input .btn{width:106px;height:32px;background:var(--green);font-size:12px;font-weight:500}
.f-head{color:var(--white);font-size:17px;font-weight:500}
.links{left:200px;top:5130px;list-style:none;color:var(--white);font-size:13px;line-height:26px}
.links li::before{content:"";display:inline-block;width:9px;height:9px;border-radius:50%;background:var(--orange);margin-right:12px}
.f-logo{left:390px;top:5140px;display:flex;align-items:center;gap:20px;color:var(--green);font-weight:700;font-size:40px;line-height:44px;letter-spacing:3px}
.f-logo .logo-mark{width:78px;height:78px;background:var(--green)}
.info{left:780px;top:5135px;color:var(--white);font-size:12px;line-height:15px}
.info .row{display:flex;gap:14px;align-items:center;margin-bottom:18px}
.info .ic{width:26px;height:26px;border-radius:50%;background:var(--orange);flex:none;display:flex;align-items:center;justify-content:center}
.bar{left:0;top:5333px;width:1200px;height:34px;background:var(--green);color:var(--white);font-size:11px;display:flex;align-items:center;justify-content:space-between;padding:0 72px 0 78px}
.social{display:flex;gap:6px}
.social span{width:26px;height:26px;border-radius:50%;border:1.5px solid var(--white)}
</style>
</head>
<body>

<div class="abs hero" role="img" aria-label="Photo of a sunlit forest canopy with large trees"></div>
<div class="abs hero-circle"></div>
<header class="abs nav">
  <div class="abs logo"><span class="logo-mark"></span><span>QUILLBY<br>TREE CARE</span></div>
  <nav class="abs menu"><span class="active">HOME</span><span>ABOUT US</span><span>SERVICES ▾</span><span>BLOG</span><span>CONTACT US</span></nav>
</header>
<h1 class="abs hero-title">Call Quillby for All Your<br>Tree Care Needs</h1>
<p class="abs hero-sub">Serving Lafayette and Surrounding Areas</p>
<a class="abs btn hero-btn">Learn More</a>

<section class="abs features">
  <div class="feature f1"><div class="ficon"></div><h3>LICENSED AND INSURED</h3><p>Lorem ipsum dolor sit amet, consectetur adip iscing elit.</p></div>
  <div class="feature f2"><div class="ficon"></div><h3>24-HOURS EMERGENCY SERVICES</h3><p>Lorem ipsum dolor sit amet, consectetur adip</p></div>
  <div class="feature f3"><div class="ficon"></div><h3>LOCALLY OWNED &amp; OPERATED</h3><p>Lorem ipsum dolor sit amet, consectetur adip</p></div>
  <div class="feature f4"><div class="ficon"></div><h3>PROFESSIONAL WORK</h3><p>Lorem ipsum dolor sit amet, consectetur adip iscing elit.</p></div>
  <div class="feature f5"><div class="ficon"></div><h3>FREE ESTIMATES</h3><p>Lorem ipsum dolor sit amet, consectetur adip iscing elit.</p></div>
</section>

<h2 class="abs sec-title about-title">About Us</h2>
<div class="abs about-text">
  <p>At Quillby Tree Care, we are more than just a tree service company, we are stewards of our beautiful trees. With a passion deeply rooted in arboriculture, we embark on a mission to promote the health, beauty, and safety of your trees and landscapes.</p>
  <p>Whether it's expert tree trimming to enhance aesthetics, meticulous tree removal to mitigate hazards, or comprehensive tree health assessments to ensure safety, we approach each task with unwavering dedication and attention to detail.</p>
</div>
<a class="abs btn about-btn">Read More</a>
<div class="abs about-img" role="img" aria-label="Circular green photo of a large tree in a forest"></div>

<h2 class="abs sec-title center services-title">Our Services</h2>
<div class="abs service" style="left:49px;top:1816px"><div class="pic"><div class="bg"></div><div class="photo p1" role="img" aria-label="Gloved hands pruning tree branches"></div></div><h4>Tree Pruning</h4></div>
<div class="abs service" style="left:409px;top:1816px"><div class="pic"><div class="bg"></div><div class="photo p2" role="img" aria-label="Chainsaw cutting a tree trunk"></div></div><h4>Tree Removal</h4></div>
<div class="abs service" style="left:768px;top:1816px"><div class="pic"><div class="bg"></div><div class="photo p3" role="img" aria-label="Arborists inspecting a tree"></div></div><h4>Tree Preservation</h4></div>
<div class="abs service" style="left:49px;top:2230px"><div class="pic"><div class="bg"></div><div class="photo p4" role="img" aria-label="Fallen tree after a storm"></div></div><h4>Emergency Services</h4></div>
<div class="abs service" style="left:409px;top:2230px"><div class="pic"><div class="bg"></div><div class="photo p5" role="img" aria-label="Worker operating a stump grinder"></div></div><h4>Stump Grinding</h4></div>
<div class="abs service" style="left:768px;top:2230px"><div class="pic"><div class="bg"></div><div class="photo p6" role="img" aria-label="Storm-damaged trees in a park"></div></div><h4>Emergency Tree Services</h4></div>

<svg class="abs cta-band" viewBox="0 0 1200 615" role="img" aria-label="Green forest photo band">
  <defs><linearGradient id="ctaGrad" x1="0" y1="0" x2="0" y2="1"><stop offset="0" stop-color="#7aa84a"/><stop offset="1" stop-color="#4f7e2c"/></linearGradient></defs>
  <path d="M0 115 Q600 -115 1200 115 L1200 490 Q600 740 0 490 Z" fill="url(#ctaGrad)"/>
</svg>
<p class="abs center cta-text">CALL US TODAY TO SEE HOW<br>WE CAN HELP YOU WITH ALL<br>OF YOUR TREE NEEDS:</p>
<a class="abs btn cta-btn">Contact Us</a>

<h2 class="abs sec-title center blog-title">Our Blog</h2>
<article class="abs card" style="left:150px"><div class="thumb t1" role="img" aria-label="Crew in safety vests working in a forest"></div><h5>Lorem ipsum dolor sit amet, consectetur elit dol</h5><p>Lorem ipsum dolor sit amet, con sectetur adipiscing elit, sed do ei</p><a class="btn">Read More</a></article>
<article class="abs card" style="left:460px"><div class="thumb t2" role="img" aria-label="Worker cutting a fallen tree"></div><h5>Lorem ipsum dolor sit amet, consectetur elit dol</h5><p>Lorem ipsum dolor sit amet, con sectetur adipiscing elit, sed do ei</p><a class="btn">Read More</a></article>
<article class="abs card" style="left:771px"><div class="thumb t3" role="img" aria-label="Close-up of a cut tree stump"></div><h5>Lorem ipsum dolor sit amet, consectetur elit dol</h5><p>Lorem ipsum dolor sit amet, con sectetur adipiscing elit, sed do ei</p><a class="btn">Read More</a></article>
<div class="abs dots"><span class="on"></span><span></span><span></span><span></span></div>

<svg class="abs contact-bg" viewBox="0 0 1200 720" role="img" aria-label="Photo of green tree canopy">
  <defs><linearGradient id="cGrad" x1="0" y1="0" x2="0" y2="1"><stop offset="0" stop-color="#5d8f34"/><stop offset="1" stop-color="#3a6a20"/></linearGradient></defs>
  <path d="M0 0 H1200 V620 Q600 740 0 620 Z" fill="url(#cGrad)"/>
</svg>
<h2 class="abs center contact-title">Contact Us</h2>
<div class="abs field" style="left:290px;top:4493px;width:620px;height:42px">Name:</div>
<div class="abs field" style="left:290px;top:4545px;width:302px;height:44px">Phone:</div>
<div class="abs field" style="left:606px;top:4545px;width:304px;height:44px">Email:</div>
<div class="abs field" style="left:290px;top:4600px;width:620px;height:81px">Mesage:</div>
<a class="abs btn submit">Submit</a>

<footer class="abs footer"></footer>
<div class="abs newsletter"><h3>Our Newsletter Sign Up</h3><div class="nl-input"><span>Enter Email Address</span><a class="btn">Signup</a></div></div>
<div class="abs f-head" style="left:203px;top:5092px">QUICK LINKS</div>
<ul class="abs links"><li>Home</li><li>About Us</li><li>Services</li><li>Blog</li><li>Contact Us</li></ul>
<div class="abs f-logo"><span class="logo-mark"></span><span>QUILLBY<br>TREE CARE</span></div>
<div class="abs f-head" style="left:780px;top:5092px">CONTACT US</div>
<div class="abs info">
  <div class="row"><span class="ic"><svg width="14" height="14" viewBox="0 0 24 24"><path d="M6.6 10.8a15 15 0 0 0 6.6 6.6l2.2-2.2a1 1 0 0 1 1-.25 11.4 11.4 0 0 0 3.6.6 1 1 0 0 1 1 1V20a1 1 0 0 1-1 1A17 17 0 0 1 3 4a1 1 0 0 1 1-1h3.5a1 1 0 0 1 1 1c0 1.25.2 2.45.6 3.6a1 1 0 0 1-.25 1z" fill="#fff"/></svg></span><span>CALL US<br>(555) 014-2739</span></div>
  <div class="row"><span class="ic"><svg width="14" height="14" viewBox="0 0 24 24"><path d="M3 5h18v14H3z" fill="#fff"/><path d="M3 5l9 7 9-7" stroke="#f7a531" stroke-width="2" fill="none"/></svg></span><span>EMAIL US<br>hello@quillbytree.com</span></div>
  <div class="row"><span class="ic"><svg width="14" height="14" viewBox="0 0 24 24"><path d="M12 2a7 7 0 0 0-7 7c0 5 7 13 7 13s7-8 7-13a7 7 0 0 0-7-7zm0 9.5A2.5 2.5 0 1 1 12 6.5a2.5 2.5 0 0 1 0 5z" fill="#fff"/></svg></span><span>Address line here dummy<br>Address line here</span></div>
</div>
<div class="abs bar"><span>Copyright ©2024– All Rights Reserved by Company name</span><div class="social"><span></span><span></span><span></span><span></span></div></div>

</body>
</html>
```